Bellcroft construction website for a high end luxury custom home builder

I need a website designed for a high end luxury custom home builder. I would like the website to host a number activities. A blog/vlog on the page where I can post about the projects being built how to's what to look out for during the build, A designated testimonial page but also having testimonials posted on the other pages like the gallery linked to the photos of the completed projects. a gallery page, an about us page, services page that demonstrate what we do and what we are capable of, and hopefully when I start winning awards, and awards page.
Home page
about us page
services page
gallery
testimonial
awards page but I my need to add that later.
I already have the domain name for the website. www.bellcroftconstruction.com.au
I recently completed a sketch hive page for my logo and will post the logo documents below.

Target Market(s)

I'd like to target professions with cash enough to build a house. I would like peolpe to understand that they are buy a price when they are getting quote to build there house. It seems like people just look for the cheapest price and end up with an inferior product. Where as people need to understand that a builder with the high price ( not astronomically higher 15-20% higher) are the ones with correct systems in place, a bide by correct OHS and use proper and correct product. If that can be conveyed through the website somehow, without saying it directly, it would be awesome.

Industry/Entity Type

Residential Construction

Coding

Coded - Design and coding required

Number of Pages Required

5+ page

Font styles to use
Sans Serif

Requirements
Must have
• I would like the testimonials to have a designated page (mentioned in the brief) but I would like the testimonials to be linked to the gallery page and when the picture are open of completed job the relevant testimonials would pop up near the pictures.

Nice to have
• I would like peolpe to understand that they are buy a price when they are getting quote to build there house. It seems like people just look for the cheapest price and end up with an inferior product. Where as people need to understand that a builder with the high price ( not astronomically higher 15-20% higher) are the ones with correct systems in place, a bide by correct OHS and use proper and correct product. If that can be conveyed through the website somehow, without saying it directly, it would be awesome.

```html
<!DOCTYPE html>
<html lang="en">
<head>
<meta charset="utf-8">
<title>Bellcroft Construction – Luxury Custom Homes</title>
<link href="https://fonts.googleapis.com/css2?family=Nunito+Sans:wght@400;600;700&display=swap" rel="stylesheet">
<style>
:root{
  --ink:#1d1d1f;
  --muted:#6b6b72;
  --faint:#b9b9c0;
  --purple:#4a23d8;
  --heading:#7b4fd6;
  --pink:#d56cd0;
  --black:#000;
  --footer:#ccffcc;
  --white:#fff;
}
*{margin:0;padding:0;box-sizing:border-box}
html,body{width:1200px;height:2600px;overflow:hidden;background:var(--white)}
body{font-family:'Nunito Sans',sans-serif;color:var(--ink);position:relative}
h1,h2,h3,h4,h5{font-weight:400}
.abs{position:absolute}
.photo{position:absolute}
.nav a{position:absolute;top:19px;font-size:7px;color:var(--ink);text-decoration:none}
.nav a.active{color:var(--pink)}
.brand{position:absolute;display:flex;align-items:center;gap:5px;font-weight:700;color:#1b4fa8;letter-spacing:.5px}
.brand .mark{background:#1b4fa8;border-radius:50%}
.hero-title{position:absolute;left:140px;width:908px;top:106px;text-align:center;font-size:26px;line-height:29px}
.hero-sub{position:absolute;left:420px;width:348px;top:177px;text-align:center;font-size:7.5px;line-height:12px;color:var(--ink)}
.search{position:absolute;left:450px;top:220px;width:288px;height:30px;background:var(--white);border-radius:15px;font-size:8px;color:var(--muted);padding:10px 12px}
.search .btn{position:absolute;right:0;top:0;width:30px;height:30px;border-radius:50%;background:var(--purple)}
.down{position:absolute;left:578px;top:340px;width:34px;height:34px;border-radius:50%;background:var(--purple);color:#fff;font-size:10px;text-align:center;line-height:34px}
.eyebrow{position:absolute;left:140px;width:908px;text-align:center;font-size:5px;letter-spacing:1px;color:var(--pink);font-weight:700}
.eyebrow span::before,.eyebrow span::after{content:"";display:inline-block;width:20px;height:1px;background:var(--pink);vertical-align:middle;margin:0 6px}
.section-title{position:absolute;left:140px;width:908px;text-align:center;font-size:17px;color:var(--heading)}
.service{position:absolute;width:120px;text-align:center}
.service h3,.step h3{font-size:9.5px;margin:0 0 8px}
.service p,.step p{font-size:6.5px;line-height:12.5px;color:var(--muted)}
.offer{position:absolute;top:684px;width:166px;height:175px}
.offer .photo{left:0;top:0;width:166px;height:107px}
.offer .info{position:absolute;left:8px;top:86px;width:125px;height:87px;background:var(--white);box-shadow:0 2px 8px rgba(0,0,0,.06);padding:12px 11px;font-size:6.5px;color:var(--muted)}
.offer .info b{color:var(--ink)}
.offer .info h4{font-size:7.5px;font-weight:600;color:var(--ink);margin:10px 0 8px}
.offer .link{position:absolute;right:0;bottom:0;width:17px;height:17px;background:var(--purple);border-radius:3px}
.step{position:absolute;width:120px;text-align:center;color:#fff}
.step p{color:#ddd}
.step .num{width:38px;height:38px;border-radius:50%;background:var(--purple);margin:0 auto 14px;font-size:13px;line-height:38px}
.body-text{font-size:6.5px;line-height:12.5px;color:var(--muted)}
.stat{position:absolute;top:1646px;display:flex;align-items:center;gap:8px}
.stat b{font-size:21px;font-weight:400}
.stat span{font-size:6.5px;line-height:8px;color:var(--muted)}
.quote{position:absolute;top:1815px;width:166px;height:104px;box-shadow:0 1px 6px rgba(0,0,0,.05);padding:10px 9px}
.quote p{font-size:6.5px;line-height:12.5px;color:var(--muted)}
.quote .who{position:absolute;left:9px;top:56px;display:flex;align-items:center;gap:6px}
.quote .avatar{width:33px;height:33px;border-radius:50%;background:#8c8f96}
.quote .who b{display:block;font-size:8px;font-weight:400}
.quote .who span{font-size:6px;color:var(--faint)}
.dots{position:absolute;left:575px;top:1938px;display:flex;gap:4px}
.dots i{width:5px;height:5px;border-radius:50%;background:#e2e2e6}
.dots i:first-child{background:var(--pink)}
.post{position:absolute;top:2090px;width:122px}
.post h4{font-size:8px;line-height:11px}
.post .meta{font-size:4.5px;color:var(--faint);margin:3px 0 9px;letter-spacing:.4px}
.post .photo{position:relative;height:86px}
.post p{font-size:6.5px;line-height:12.5px;color:var(--muted);margin-top:9px}
.footer{position:absolute;left:140px;top:2325px;width:908px;height:275px;background:var(--footer)}
.footer h5{position:absolute;top:53px;font-size:8.5px}
.footer ul{position:absolute;top:80px;list-style:none;font-size:6.5px;line-height:12.5px}
.footer li::before{content:"→ ";color:var(--pink)}
.footer .social{position:absolute;top:111px;width:8px;height:8px;border-radius:50%;background:var(--pink)}
.contact{position:absolute;left:640px;font-size:6.5px;line-height:10px}
.contact.pinked{color:var(--pink)}
.copyright{position:absolute;left:0;width:908px;top:189px;text-align:center;font-size:6.5px}
</style>
</head>
<body>

<header>
  <div class="photo" role="img" aria-label="Hero photo of white architect-designed homes framing the sky" style="left:140px;top:0;width:908px;height:366px;background:linear-gradient(180deg,#e9edf4 0%,#f7f8fb 45%,#d7dbe3 100%)"></div>
  <svg class="abs" style="left:140px;top:320px" width="908" height="50"><path d="M0 42 Q454 18 908 42 L908 50 L0 50Z" fill="#fff"/><path d="M0 42 L40 44" stroke="#333" stroke-width="1"/><path d="M868 44 L908 42" stroke="#333" stroke-width="1"/></svg>
  <div class="brand" style="left:234px;top:20px;font-size:12px"><i class="mark" style="width:14px;height:14px"></i>BELLCROFT</div>
  <nav class="nav">
    <a class="active" style="left:657px">Home</a>
    <a style="left:692px">About Us</a>
    <a style="left:737px">Services</a>
    <a style="left:778px">Gallery</a>
    <a style="left:816px">Testimonial</a>
  </nav>
  <h1 class="hero-title">The Considered<br>Way to Build Your Home</h1>
  <p class="hero-sub">Luxury custom homes built with proven systems, certified trades and premium materials, so every detail is made to last for generations</p>
  <div class="search">Search our completed homes<span class="btn"><svg width="30" height="30"><circle cx="14" cy="14" r="4" fill="none" stroke="#fff" stroke-width="1.4"/><path d="M17 17 L20 20" stroke="#fff" stroke-width="1.4"/></svg></span></div>
  <div class="down">↓</div>
</header>

<section class="services">
  <div class="eyebrow" style="top:410px"><span>OUR SERVICES</span></div>
  <h2 class="section-title" style="top:422px">The smartest way to build a home</h2>
  <svg class="abs" style="left:380px;top:474px" width="28" height="26"><path d="M3 24 V12 L14 3 L25 12 V24Z" fill="none" stroke="#d56cd0" stroke-width="1.2"/><rect x="11" y="16" width="6" height="8" fill="none" stroke="#d56cd0" stroke-width="1.2"/></svg>
  <svg class="abs" style="left:514px;top:474px" width="28" height="26"><rect x="1" y="6" width="24" height="18" rx="2" fill="none" stroke="#d56cd0" stroke-width="1.2"/><path d="M1 12 H25 M9 6 V24 M17 12 V24" stroke="#d56cd0" stroke-width="1.2"/></svg>
  <svg class="abs" style="left:650px;top:472px" width="24" height="28"><rect x="2" y="2" width="20" height="24" fill="none" stroke="#d56cd0" stroke-width="1.2"/><path d="M6 9h12M6 13h12M6 17h12M6 21h8" stroke="#d56cd0"/></svg>
  <svg class="abs" style="left:786px;top:472px" width="22" height="28"><path d="M5 12 V7 a6 6 0 0 1 12 0 V12" fill="none" stroke="#d56cd0" stroke-width="1.2"/><rect x="2" y="12" width="18" height="14" fill="none" stroke="#d56cd0" stroke-width="1.2"/></svg>
  <div class="service" style="left:333px;top:516px"><h3>Custom Design</h3><p>Every home starts with your brief, shaped with our architects into plans made for your site.</p></div>
  <div class="service" style="left:467px;top:516px"><h3>Premium Materials</h3><p>Certified products from trusted suppliers, chosen to perform in every season for decades.</p></div>
  <div class="service" style="left:602px;top:516px"><h3>Experts in Your Corner</h3><p>Licensed trades and one site manager who knows your build from slab to handover.</p></div>
  <div class="service" style="left:736px;top:516px"><h3>Locked in Quality</h3><p>Documented safety systems and staged inspections at every step of the build.</p></div>
</section>

<section class="offers">
  <div class="eyebrow" style="top:624px"><span>WHAT WE BUILD</span></div>
  <h2 class="section-title" style="top:636px">Recent Custom Homes</h2>
  <article class="offer" style="left:332px"><div class="photo" role="img" aria-label="Photo of a bright living room in a completed home" style="background:linear-gradient(135deg,#d9d6d1,#8f8a85)"></div><div class="info">Completed &nbsp; <b>2024</b> · 14 mths<div style="margin-top:10px">▭ 4 &nbsp; ◡ 3 &nbsp; ▣ 420 sqm</div><h4>The Ridgeline Residence</h4>Harwick Vale</div><span class="link"></span></article>
  <article class="offer" style="left:511px"><div class="photo" role="img" aria-label="Photo of a custom white kitchen" style="background:linear-gradient(135deg,#e6e6e4,#a5a3a0)"></div><div class="info">Completed &nbsp; <b>2023</b> · 12 mths<div style="margin-top:10px">▭ 5 &nbsp; ◡ 4 &nbsp; ▣ 510 sqm</div><h4>The Harbour View Home</h4>Harwick Vale</div><span class="link"></span></article>
  <article class="offer" style="left:691px"><div class="photo" role="img" aria-label="Photo of a timber staircase beside tall windows" style="background:linear-gradient(135deg,#cfd6de,#8b7a62)"></div><div class="info">Completed &nbsp; <b>2023</b> · 16 mths<div style="margin-top:10px">▭ 4 &nbsp; ◡ 3 &nbsp; ▣ 465 sqm</div><h4>The Stonegate House</h4>Harwick Vale</div><span class="link"></span></article>
</section>

<section class="workflow">
  <svg class="abs" style="left:161px;top:925px" width="867" height="422"><path d="M0 0 H434 V418 L0 392Z" fill="#000"/><path d="M0 392 L0 420 M0 420 L30 421" stroke="#333"/><path d="M867 392 L867 420 M837 421 L867 420" stroke="#333"/></svg>
  <div class="photo" role="img" aria-label="Photo of a living room with a stone fireplace and city view windows" style="left:595px;top:925px;width:433px;height:418px;background:linear-gradient(135deg,#8e8a86,#5c524a 60%,#3d342d);clip-path:polygon(0 0,100% 0,100% 94%,0 100%)"></div>
  <div class="eyebrow" style="left:161px;width:600px;top:968px"><span>WORK FLOW</span></div>
  <h2 class="abs" style="left:161px;width:600px;top:981px;text-align:center;font-size:17px;color:#fff">How it works</h2>
  <div class="step" style="left:333px;top:1042px"><div class="num">01</div><h3>Design Consultation</h3><p>We walk your site, learn how you live and set a clear brief and budget together.</p></div>
  <div class="step" style="left:467px;top:1042px"><div class="num">02</div><h3>Plans &amp; Approvals</h3><p>Detailed drawings, engineering and permits handled before a single trade arrives.</p></div>
  <div class="step" style="left:333px;top:1164px"><div class="num">03</div><h3>Build with Care</h3><p>Safe, tidy sites, certified trades and weekly updates as your home takes shape.</p></div>
  <div class="step" style="left:467px;top:1164px"><div class="num">04</div><h3>Move Into Your Home</h3><p>A thorough handover, full warranties and support long after you get the keys.</p></div>
</section>

<section class="about">
  <div class="photo" role="img" aria-label="Photo of a family gathered outdoors at dusk" style="left:332px;top:1387px;width:263px;height:243px;background:linear-gradient(180deg,#8a8f96,#b99a86 45%,#4f4640)"></div>
  <div class="abs" style="left:543px;top:1407px;width:317px;height:203px;background:#fff;padding:24px 21px">
    <h2 style="font-size:17px;color:var(--heading);margin-bottom:14px">We Put People First.</h2>
    <p class="body-text" style="margin-bottom:7px">A home is the largest investment most families will make. We treat it that way, with honest advice, clear timelines and a team that answers the phone.</p>
    <p class="body-text">Behind every Bellcroft home sits a system built over many years: documented safety plans on every site, licensed and insured trades, staged quality inspections and products chosen because they are correct for the job, not because they are the cheapest on the shelf. That care shows in the details you see on handover day, and in the ones you never have to think about again, from waterproofing and framing to the wiring inside the walls. It is why so many of our clients come to us through the friends and neighbours we built for first.</p>
  </div>
  <div class="stat" style="left:332px"><b>305</b><span>Homes<br>Completed</span></div>
  <div class="stat" style="left:467px"><b>1,090</b><span>Site<br>Inspections</span></div>
  <div class="stat" style="left:601px"><b>209</b><span>Licensed<br>Trades</span></div>
  <div class="stat" style="left:736px"><b>67</b><span>Repeat<br>Clients</span></div>
  <div class="abs" style="left:453px;top:1640px;width:1px;height:32px;background:#eee"></div>
  <div class="abs" style="left:588px;top:1640px;width:1px;height:32px;background:#eee"></div>
  <div class="abs" style="left:722px;top:1640px;width:1px;height:32px;background:#eee"></div>
</section>

<section class="testimonials">
  <div class="eyebrow" style="top:1745px"><span>TESTIMONIAL</span></div>
  <h2 class="section-title" style="top:1757px">Happy Clients</h2>
  <div class="quote" style="left:332px"><p>The site was spotless every visit and the finish is flawless. Worth every cent we invested in our home.</p><div class="who"><i class="avatar" role="img" aria-label="Client portrait"></i><div><b>Dana Whitlow</b><span>Homeowner</span></div></div></div>
  <div class="quote" style="left:511px"><p>The site was spotless every visit and the finish is flawless. Worth every cent we invested in our home.</p><div class="who"><i class="avatar" role="img" aria-label="Client portrait"></i><div><b>Dana Whitlow</b><span>Homeowner</span></div></div></div>
  <div class="quote" style="left:691px"><p>The site was spotless every visit and the finish is flawless. Worth every cent we invested in our home.</p><div class="who"><i class="avatar" role="img" aria-label="Client portrait"></i><div><b>Dana Whitlow</b><span>Homeowner</span></div></div></div>
  <div class="dots"><i></i><i></i><i></i><i></i><i></i></div>
</section>

<section class="blog">
  <div class="eyebrow" style="top:2031px"><span>BLOG</span></div>
  <h2 class="section-title" style="top:2042px">Recent Blog</h2>
  <article class="post" style="left:332px"><h4>What to Check Before Your Bathroom Is Tiled</h4><div class="meta">JULY. 24, 2024 &nbsp; ADMIN &nbsp; ▪ 3</div><div class="photo" role="img" aria-label="Photo of a freestanding bathtub in a concrete bathroom" style="background:linear-gradient(135deg,#b3aca5,#6e655d)"></div><p>Waterproofing is the step you never see, and the one worth checking twice.</p></article>
  <article class="post" style="left:466px"><h4>Inside the Build: Framing the Harbour View Home</h4><div class="meta">JULY. 18, 2024 &nbsp; ADMIN &nbsp; ▪ 3</div><div class="photo" role="img" aria-label="Photo of a long dark corridor" style="background:linear-gradient(135deg,#5a6068,#2b2f35)"></div><p>A walk through the frame stage and the inspections we complete on site.</p></article>
  <article class="post" style="left:601px"><h4>How to Read a Building Quote the Right Way</h4><div class="meta">JULY. 10, 2024 &nbsp; ADMIN &nbsp; ▪ 3</div><div class="photo" role="img" aria-label="Photo of a white room lined with bookshelves" style="background:linear-gradient(135deg,#e8e4de,#9c7d5c)"></div><p>What is included, what is left out and the questions to ask every builder.</p></article>
  <article class="post" style="left:736px"><h4>Choosing Lighting That Suits a Custom Home</h4><div class="meta">JULY. 02, 2024 &nbsp; ADMIN &nbsp; ▪ 3</div><div class="photo" role="img" aria-label="Photo of warm pendant lights and plants" style="background:linear-gradient(135deg,#c98b4f,#3a2a1e)"></div><p>Layered light plans that make each room feel warm, calm and well made.</p></article>
</section>

<footer class="footer">
  <div class="brand" style="left:32px;top:56px;font-size:17px"><i class="mark" style="width:22px;height:22px"></i>BELLCROFT</div>
  <p class="abs" style="left:192px;top:50px;width:100px;font-size:6.5px;line-height:12.5px">Luxury custom homes, built properly from the ground up.</p>
  <i class="social" style="left:199px"></i><i class="social" style="left:226px"></i><i class="social" style="left:254px"></i>
  <h5 style="left:310px">Community</h5>
  <ul style="left:310px"><li>Our Projects</li><li>Testimonials</li><li>Build Journal</li><li>FAQs</li></ul>
  <h5 style="left:418px">About Us</h5>
  <ul style="left:416px"><li>Our Story</li><li>Meet the team</li><li>Careers</li></ul>
  <h5 style="left:515px">Company</h5>
  <ul style="left:514px"><li>Services</li><li>Gallery</li><li>Contact</li><li>Awards</li></ul>
  <h5 style="left:622px">Have a Questions?</h5>
  <svg class="abs" style="left:622px;top:80px" width="8" height="10"><path d="M4 10 L1 5 a3 3 0 1 1 6 0Z" fill="#d56cd0"/></svg>
  <p class="contact" style="top:80px;width:80px">48 Larchmere Rd. Harwick Vale, Tasmania, Australia</p>
  <svg class="abs" style="left:622px;top:118px" width="8" height="8"><path d="M1 1 L3 1 L4 3 L3 4 Q4 6 5 5 L6 4 L8 5 L8 7 Q3 8 1 1Z" fill="#d56cd0"/></svg>
  <p class="contact pinked" style="top:118px">+61 3 5550 1842</p>
  <svg class="abs" style="left:622px;top:141px" width="9" height="7"><rect width="9" height="7" fill="#d56cd0"/><path d="M0 0 L4.5 4 L9 0" stroke="#fff" fill="none"/></svg>
  <p class="contact pinked" style="top:140px">hello@bellcroftbuild.com</p>
  <p class="copyright">Copyright ©2024 All rights reserved | Bellcroft Construction · www.bellcroftconstruction.com.au</p>
</footer>

</body>
</html>
```